Letterhead

Can you please design me a letterhead that I can use electronically in word as a template. I have attached my business card as I would like the design to reflect this logo.

```html
<!DOCTYPE html>
<html lang="en">
<head>
<meta charset="utf-8">
<title>Meridale Letterhead</title>
<link rel="stylesheet" href="https://fonts.googleapis.com/css2?family=Open+Sans:wght@400&family=Arimo:wght@400&display=swap">
<style>
  :root {
    --brand-red: #b93a3e;
    --charcoal: #3a3536;
    --text-grey: #4a4a4a;
    --page-border: #333333;
    --paper: #ffffff;
  }
  * { margin: 0; padding: 0; box-sizing: border-box; }
  html, body {
    width: 1200px;
    height: 1000px;
    overflow: hidden;
    background: var(--paper);
  }
  .canvas {
    position: relative;
    width: 1200px;
    height: 1000px;
  }
  .sheet {
    position: absolute;
    left: 241px;
    top: 34px;
    width: 718px;
    height: 932px;
    border: 1px solid var(--page-border);
    background: var(--paper);
  }
  .rule {
    position: absolute;
    height: 12px;
    background: var(--brand-red);
  }
  .rule::after {
    content: "";
    position: absolute;
    left: 0;
    right: 0;
    top: 14px;
    height: 3px;
    background: var(--charcoal);
  }
  .rule--header-left { left: 17px; top: 61px; width: 255px; }
  .rule--header-right { left: 446px; top: 61px; width: 255px; }
  .rule--footer { left: 17px; top: 890px; width: 684px; }

  .brand {
    position: absolute;
    left: 272px;
    top: 44px;
    width: 174px;
    text-align: center;
  }
  .brand__name {
    display: block;
    font-family: "Open Sans", sans-serif;
    font-weight: 400;
    font-size: 37px;
    line-height: 42px;
    letter-spacing: 0.5px;
    color: var(--brand-red);
  }
  .brand__tagline {
    display: block;
    margin-top: 4px;
    font-family: "Arimo", Arial, sans-serif;
    font-size: 8.5px;
    color: var(--charcoal);
    text-align: left;
    padding-left: 9px;
  }

  .contact-line {
    position: absolute;
    left: 0;
    right: 0;
    top: 862px;
    text-align: center;
    font-family: "Open Sans", sans-serif;
    font-size: 15px;
    color: var(--text-grey);
    white-space: nowrap;
  }
  .contact-line__label { color: var(--brand-red); }
  .contact-line__divider {
    color: var(--brand-red);
    margin: 0 4px;
  }
</style>
</head>
<body>
  <div class="canvas">
    <div class="sheet">
      <div class="rule rule--header-left"></div>
      <div class="brand">
        <span class="brand__name">meridale</span>
        <span class="brand__tagline">Business Consultants Pty Ltd</span>
      </div>
      <div class="rule rule--header-right"></div>

      <p class="contact-line">
        <span class="contact-line__label">P</span> : 0400 518 342
        <span class="contact-line__divider">|</span>
        <span class="contact-line__label">E</span> : office@meridale.net.au
        <span class="contact-line__divider">|</span>
        <span class="contact-line__label">ACN</span> : 081 462 935
      </p>
      <div class="rule rule--footer"></div>
    </div>
  </div>
</body>
</html>
```